Business Card Design

Quiet Fernlight - edgy, unique, ontrend clothing for girls 0-12.
I would like simple styling with white background and natural beige/brown font, similar to attached font.

Industry/Entity Type

Clothing

Contact Information for Business Card

Hi, I would like a very simple business card, white background with natural, beige, brown font, Quiet Fernlight. I design and sell clothes for girls 0-12 with a touch of bohemian styling. I would like "Quiet Fernlight" on front and on back -
www.quietfernlight.example.au
Colette Brennick,
0491558213,
colettebrennick@mailvale.example.au

```html
<!DOCTYPE html>
<html lang="en">
<head>
<meta charset="utf-8">
<title>Quiet Fernlight – Business Cards</title>
<link href="https://fonts.googleapis.com/css2?family=Comfortaa:wght@400;600;700&display=swap" rel="stylesheet">
<style>
  :root {
    --page-bg: #efece6;
    --card-base: #e4dccd;
    --card-warm: #ebdcb4;
    --card-cool: #d9d3c8;
    --ink-name: #9a8548;
    --ink-detail: #a08d57;
    --ink-brand: #8d8670;
    --card-shadow: rgba(60, 45, 25, 0.18);
  }
  * { margin: 0; padding: 0; box-sizing: border-box; }
  html, body {
    width: 1200px;
    height: 960px;
    overflow: hidden;
    background: var(--page-bg);
    font-family: "Comfortaa", sans-serif;
  }
  .sheet {
    position: relative;
    width: 1200px;
    height: 960px;
  }
  .card {
    position: absolute;
    left: 290px;
    width: 620px;
    height: 380px;
    overflow: hidden;
    box-shadow: 0 10px 26px var(--card-shadow);
  }
  .card--back { top: 80px; }
  .card--front { top: 500px; }
  .card-pattern {
    position: absolute;
    inset: 0;
    background:
      radial-gradient(circle at 22% 30%, var(--card-warm) 0, transparent 22%),
      radial-gradient(circle at 78% 70%, var(--card-warm) 0, transparent 24%),
      radial-gradient(circle at 50% 55%, var(--card-cool) 0, transparent 35%),
      var(--card-base);
  }
  .card-text {
    position: absolute;
    white-space: nowrap;
  }
  .contact-name {
    top: 38px;
    right: 70px;
    font-size: 30px;
    font-weight: 600;
    color: var(--ink-name);
    letter-spacing: 1px;
  }
  .contact-email {
    top: 100px;
    left: 36px;
    font-size: 13px;
    color: var(--ink-detail);
  }
  .contact-web {
    top: 132px;
    right: 36px;
    font-size: 14px;
    color: var(--ink-detail);
  }
  .contact-phone {
    top: 160px;
    left: 270px;
    font-size: 15px;
    color: var(--ink-detail);
    letter-spacing: 1px;
  }
  .brand-name {
    font-size: 46px;
    font-weight: 700;
    color: var(--ink-brand);
    letter-spacing: 1px;
  }
  .card--back .brand-name { top: 262px; right: 40px; }
  .card--front .brand-name { top: 250px; left: 60px; }
</style>
</head>
<body>
  <main class="sheet">
    <section class="card card--back" aria-label="Business card back">
      <div class="card-pattern" role="img" aria-label="Soft beige and gold bohemian medallion pattern background"></div>
      <p class="card-text contact-name">Colette Brennick</p>
      <p class="card-text contact-email">colettebrennick@mailvale.example.au</p>
      <p class="card-text contact-web">www.quietfernlight.example.au</p>
      <p class="card-text contact-phone">0491558213</p>
      <p class="card-text brand-name">Quiet Fernlight</p>
    </section>
    <section class="card card--front" aria-label="Business card front">
      <div class="card-pattern" role="img" aria-label="Soft beige and gold bohemian medallion pattern background"></div>
      <p class="card-text brand-name">Quiet Fernlight</p>
    </section>
  </main>
</body>
</html>
```